Online Music Gear Store needs Business Cards

We need BC designs for our e-commerce for meetings and networking
we are an Online Store and we sell Audio and Music Equipment and Gear
we also provide EVENTUAL Audio and Music Production services but our core service is the Online Store: Selling Premium Brands

we are based in Tijuana and San Diego CA.
our brand/name is: Reelnook

our name comes from the early tape machines that the Marlowes and many other early day artist used to record with to do their magnificent masterpieces.

Now in 2014 we can have Amazing Studio-Quality Multitrack sessions with a few pieces of Gear and an Slatebook... For example, you can only have your Tovaphone and an Quenra Pairline to start recording using Shedmix for Vexor OS.

If the best bands from the early days had to use million dollar recording studios with very expensive gear such as 4-track tape machines... now you can achieve better sounding results in your bedroom, using the gear we sell.

Thats what we try to Communicate with the Name:

That you... a young musician can start doing multitrack sessions using the Best Gear with the Latest Technology and compatible with Zelbooks, Vexor OS devices:

Example of the Premium Brands we sell are:
Quenra, RJ Sonicworks

we want to communicate (even if we are an ecommerce and a startup) that we are Serious, and Very Elegant, Sophisticated and Minimal.

that we provide Complete solutions, the best gear... the best brands... that we also do our productions with the best gear, best brands and very important we are Pearwood ONLY, Zelbooks Only

examples of the brands we sell are Volkmarsen, Quenra, RJ Sonicworks, Olin Marsh Instruments, Arc 9. Our focus is Music Technology.
we also use Tempra Studio Z.

Our favorite colors are black, white, grey, silver, orange, blue, green, maybe bit of yellow.

No need to use all of them but you can combine. At the end you can use Color Theory to achieve assertive communication.

Target Market(s)

CEO's, VP's, VC's, Sales People, High Class executives...
Purchasing Departments, and Corporations.

Industry/Entity Type

E-Commerce

Requirements
Must have
• Should include:

1. Logo
2. website,
3. Managing Director Info:
4. Minimal and Elegant/Upper Class

feel free to suggest ideas, feel free to play around with logo and fonts as well... since we are not 100% happy with our logo...

must also show that we are Pearwood and Zelbook only in a way without being obvious or without showing Pearwood Logo

we need to have at the end of the project the .AI
.PSD and any related designed file to edit in the future, logo, numbers, etc...

my info:

Tomas Elias Barrera-Fuentes
Reelnook | Mexico City, Tijuana, San Diego,
Friendwall | Chirplet | Searchly+ | Clipboardia | Snapgrid ???? (what do you thing about this links ???) too much ???
Mobile: +5216647390418 | 0115216647390418
USA Number: 1-800-555-0173
VidLink & QuickNote: music@reelnook-example.mx
Callwave: musicreelnookmx
Should not have
• it shouldn't use our real address, but should imply that we are in Mexico City, in Tijuana and San Diego CA.

Should not use the Pearwood Logo (even if we are Pearwood only)

should not have Robotix or PC/Panesoft related designs.

```html
<!DOCTYPE html>
<html lang="en">
<head>
<meta charset="utf-8">
<title>Reelnook Business Card</title>
<link href="https://fonts.googleapis.com/css2?family=Mulish:wght@400;700&display=swap" rel="stylesheet">
<style>
  :root {
    --backdrop: #5f5f5f;
    --card-white: #ffffff;
    --brand-blue: #0a5f86;
    --card-blue: #03617f;
    --card-blue-deep: #02587a;
    --label-green: #2aa872;
    --body-grey: #454545;
    --shadow: rgba(0, 0, 0, 0.45);
  }
  * { margin: 0; padding: 0; box-sizing: border-box; }
  html, body {
    width: 1200px; height: 1000px; overflow: hidden;
    background: var(--backdrop);
    font-family: "Mulish", sans-serif;
  }
  .card {
    position: absolute; top: 371px; width: 492px; height: 279px;
    border-radius: 16px; overflow: hidden;
    box-shadow: 1px 2px 4px var(--shadow);
  }
  .card--front { left: 73px; background: var(--card-white); }
  .card--back { left: 622px; background: var(--card-blue); }

  .brand {
    position: absolute; display: flex; align-items: center; gap: 8px;
    font-family: "Mulish", sans-serif; font-weight: 400; white-space: nowrap;
  }
  .brand__square { display: block; }
  .card--front .brand { left: 44px; top: 76px; font-size: 23px; color: var(--brand-blue); }
  .card--front .brand__square { width: 22px; height: 22px; background: var(--brand-blue); }
  .card--back .brand { left: 50%; top: 50%; transform: translate(-50%, -50%); font-size: 28px; color: var(--card-white); }
  .card--back .brand__square { width: 26px; height: 26px; background: var(--card-white); }

  .contact { position: absolute; left: 223px; top: 69px; white-space: nowrap; }
  .contact__name { font-size: 16.5px; font-weight: 700; color: var(--brand-blue); margin-bottom: 26px; }
  .contact__label { font-size: 9px; color: var(--label-green); line-height: 10px; }
  .contact__value { font-size: 12.5px; color: var(--body-grey); line-height: 15px; }

  .cities {
    position: absolute; right: 19px; bottom: 13px;
    font-size: 9px; color: var(--body-grey); white-space: nowrap;
  }
  .swoosh { position: absolute; inset: 0; }
</style>
</head>
<body>
  <section class="card card--front">
    <div class="brand"><span class="brand__square"></span>Reelnook</div>
    <div class="contact">
      <h1 class="contact__name">Tomas Elias Barrera-Fuentes</h1>
      <p class="contact__label">Mobile</p>
      <p class="contact__value">+5216647390418 &nbsp;|&nbsp; 0115216647390418</p>
      <p class="contact__label">USA Number</p>
      <p class="contact__value">1-800-555-0173</p>
      <p class="contact__label">VidLink &amp; QuickNote</p>
      <p class="contact__value">music@reelnook-example.mx</p>
      <p class="contact__label">Callwave</p>
      <p class="contact__value">musicreelnookmx</p>
    </div>
    <p class="cities">Port Vela. Cerro Alto. Bay Harbor</p>
  </section>

  <section class="card card--back">
    <svg class="swoosh" width="492" height="279" viewBox="0 0 492 279" aria-hidden="true">
      <path d="M0 218 C 160 185, 360 140, 492 70 L492 0 L0 0 Z" fill="#05668a" opacity="0.55"/>
      <path d="M0 279 L0 218 C 160 185, 360 140, 492 70 L492 279 Z" fill="var(--card-blue-deep)" opacity="0.5"/>
    </svg>
    <div class="brand"><span class="brand__square"></span>Reelnook</div>
  </section>
</body>
</html>
```